Web Design Project - Old Larchmere (Bar)

We need a website for a new wine bar/hotel opening in Sydney's Kings Cross area. The concept is a rustic Australiana bar. We intend to use raw materials (sandstone, rusty metal etc) and lots of greenery/plants. It is set to be stylish and accessible to a young and middle age clientele.

The idea is to bring the outside inside.

The venue can cater for 450 people and is in one of the major nightclub strips in Australia. The demographic differs from celebrities to backpackers.
Updates

Target Market(s)

We are targeting 23yr - 40yr olds.

Industry/Entity Type

Hotel

Requirements
Must have
• What I want is a design to reflect is the fit out of the bar. We would like to see a rustic design to reflect the theme of the bar. The theme behind the fit out will be "bringing the outside inside" with lots of plants, wet walls etc.. There will be exposed brickwork, sandstone, timber and rusted steel with laser cut designs throughout the venue.
Nice to have
• I've attached some 3D designs that the venue will be roughly based on.

```html
<!DOCTYPE html>
<html lang="en">
<head>
<meta charset="utf-8">
<title>Old Larchmere</title>
<link rel="stylesheet" href="https://fonts.googleapis.com/css2?family=Federo&family=Arimo:wght@400;700&display=swap">
<style>
  :root {
    --nav-bg: #1e1813;
    --nav-text: #bdb3a4;
    --white: #ffffff;
    --accent: #d9cf3a;
    --arrow: #b8c22e;
    --leaf: #7fa83a;
    --sandstone: #c9b48e;
    --timber: #4a3726;
    --rust: #8a4a24;
    --logo-bg: #7a6248;
    --logo-ink: #1c1611;
    --btn: #0d0b09;
    --frame: #cfc6b6;
  }
  * { margin: 0; padding: 0; box-sizing: border-box; }
  html, body { width: 1200px; height: 900px; overflow: hidden; }
  body { position: relative; font-family: "Arimo", Arial, sans-serif; color: var(--white); background: #5e5449; }
  .abs { position: absolute; }

  .backdrop { left: 0; top: 47px; width: 1200px; height: 853px;
    background: linear-gradient(100deg, #8c8273 0%, #6e6457 35%, #5c5348 55%, #6d6a4c 80%, #8f8a48 100%); }
  .header-band { left: 0; top: 47px; width: 1200px; height: 158px;
    background: linear-gradient(90deg, rgba(214,196,160,0.75), rgba(190,172,136,0.55) 60%, rgba(160,150,100,0.45)); }
  .content-band { left: 0; top: 205px; width: 1200px; height: 593px; background: rgba(52,44,36,0.35); }
  .footer-band { left: 0; top: 798px; width: 1200px; height: 102px;
    background: linear-gradient(180deg, rgba(58,44,32,0.75), rgba(40,30,22,0.85)); border-top: 1px solid #a8a23a; }

  .topnav { left: 0; top: 0; width: 1200px; height: 47px; background: var(--nav-bg); border-top: 2px solid #33291f; }
  .topnav a { position: absolute; top: 13px; font-size: 13.5px; color: var(--nav-text); text-decoration: none; }
  .topnav a.current { color: var(--white); }
  .nav-marker { left: 161px; top: 32px; }
  .search-field { left: 769px; top: 13px; width: 200px; height: 20px; background: #2c241d; border: 1px solid #5a4e42; }
  .search-btn { left: 978px; top: 13px; width: 72px; height: 20px; background: #2c241d; border: 1px solid #5a4e42; color: var(--nav-text); font-size: 13px; text-align: center; line-height: 18px; }

  .brand { left: 150px; top: 66px; width: 209px; height: 125px; background: var(--logo-bg); border: 1px solid #3c3024;
    display: flex; align-items: center; justify-content: center; gap: 8px; }
  .brand-square { width: 12px; height: 12px; background: var(--logo-ink); flex: none; }
  .brand-name { font-family: "Federo", sans-serif; font-size: 19px; color: var(--logo-ink); letter-spacing: 0.5px; white-space: nowrap; }

  .heading { font-family: "Federo", sans-serif; font-size: 22px; font-weight: 400; color: var(--white); white-space: nowrap; }
  .heading.accent { color: var(--accent); }

  .photo { width: 252px; height: 147px; border: 2px solid var(--frame); box-shadow: 0 2px 6px rgba(0,0,0,0.5); }
  .photo-grapes { background: linear-gradient(135deg, #3e2c1e, #6e5230 45%, #6f8a3a 75%, #b59a58); }
  .photo-bottles { background: linear-gradient(120deg, #24180e, #6e4218 45%, #c2932e 80%, #3a2410); }

  .blurb { width: 302px; font-size: 12.5px; line-height: 19px; text-align: justify; }
  .btn { height: 21px; background: var(--btn); color: var(--white); font-size: 9px; letter-spacing: 0.5px; text-align: center; line-height: 21px; }

  .menu-list { left: 884px; top: 268px; list-style: none; }
  .menu-list li { height: 29.8px; font-size: 13px; display: flex; align-items: center; white-space: nowrap; }
  .menu-list svg { margin-right: 22px; }

  .about-text { left: 147px; top: 651px; width: 692px; font-size: 12.5px; line-height: 19px; text-align: justify; hyphens: auto; }
  .contact-lines { left: 916px; top: 648px; font-size: 11px; line-height: 23.5px; font-style: normal; }

  .footnav { left: 0; top: 823px; width: 1200px; text-align: center; font-size: 14px; }
  .footnav a { color: var(--white); text-decoration: none; margin: 0 17px; }
  .copyright { left: 0; top: 864px; width: 1200px; text-align: center; font-size: 10px; }
</style>
</head>
<body>
  <div class="abs backdrop" role="img" aria-label="Photograph of white wine pouring from a dark bottle into a glass"></div>
  <div class="abs header-band"></div>
  <div class="abs content-band"></div>
  <div class="abs footer-band"></div>

  <nav class="abs topnav">
    <a class="current" href="#" style="left:149px">Home</a>
    <a href="#" style="left:220px">About Us</a>
    <a href="#" style="left:309px">Menu</a>
    <a href="#" style="left:377px">Events</a>
    <a href="#" style="left:453px">Contact Us</a>
    <svg class="abs nav-marker" width="12" height="7" viewBox="0 0 12 7"><polygon points="6,0 12,7 0,7" fill="var(--leaf)"/></svg>
    <div class="abs search-field"></div>
    <div class="abs search-btn">Search</div>
  </nav>

  <div class="abs brand"><span class="brand-square"></span><span class="brand-name">OLD LARCHMERE</span></div>

  <h2 class="abs heading" style="left:147px;top:226px">Lorem Ipsum</h2>
  <div class="abs photo photo-grapes" style="left:173px;top:280px" role="img" aria-label="Photograph of wine bottles, grapes and cheese on a timber barrel"></div>
  <p class="abs blurb" style="left:149px;top:456px">Lorem Ipsum is simply dummy text of the printing and typesetting industry. Lorem Ipsum has been the industry's standard dummy text ever since the 1500s, when an unknown printer took a galley</p>
  <div class="abs btn" style="left:372px;top:547px;width:78px">Read More...</div>

  <h2 class="abs heading" style="left:502px;top:226px">Lorem Ipsum is simply</h2>
  <div class="abs photo photo-bottles" style="left:527px;top:280px" role="img" aria-label="Photograph of wine bottles lying in a rack"></div>
  <p class="abs blurb" style="left:504px;top:456px">Lorem Ipsum is simply dummy text of the printing and typesetting industry. Lorem Ipsum has been the industry's standard dummy text ever since the 1500s, when an unknown printer took a galley</p>
  <div class="abs btn" style="left:726px;top:547px;width:78px">Read More...</div>

  <h2 class="abs heading" style="left:860px;top:226px">Our Menu</h2>
  <ul class="abs menu-list">
    <li><svg width="7" height="9" viewBox="0 0 7 9"><polygon points="0,0 7,4.5 0,9" fill="var(--arrow)"/></svg>Share Plates</li>
    <li><svg width="7" height="9" viewBox="0 0 7 9"><polygon points="0,0 7,4.5 0,9" fill="var(--arrow)"/></svg>Bar Snacks</li>
    <li><svg width="7" height="9" viewBox="0 0 7 9"><polygon points="0,0 7,4.5 0,9" fill="var(--arrow)"/></svg>Garden Salads</li>
    <li><svg width="7" height="9" viewBox="0 0 7 9"><polygon points="0,0 7,4.5 0,9" fill="var(--arrow)"/></svg>Wood-fired Mains</li>
    <li><svg width="7" height="9" viewBox="0 0 7 9"><polygon points="0,0 7,4.5 0,9" fill="var(--arrow)"/></svg>Cheese Boards</li>
    <li><svg width="7" height="9" viewBox="0 0 7 9"><polygon points="0,0 7,4.5 0,9" fill="var(--arrow)"/></svg>Freshly Baked Breads</li>
    <li><svg width="7" height="9" viewBox="0 0 7 9"><polygon points="0,0 7,4.5 0,9" fill="var(--arrow)"/></svg>Australian Specials</li>
    <li><svg width="7" height="9" viewBox="0 0 7 9"><polygon points="0,0 7,4.5 0,9" fill="var(--arrow)"/></svg>Desserts</li>
    <li><svg width="7" height="9" viewBox="0 0 7 9"><polygon points="0,0 7,4.5 0,9" fill="var(--arrow)"/></svg>Wines by the Glass</li>
  </ul>
  <div class="abs btn" style="left:994px;top:547px;width:57px">More...</div>

  <h2 class="abs heading accent" style="left:148px;top:614px">About OLD LARCHMERE</h2>
  <p class="abs about-text" lang="en">Lorem Ipsum is simply dummy text of the printing and typesetting industry. Lorem Ipsum has been the industry's standard dummy text ever since the 1500s, when an unknown printer took a galley of type and scrambled it to make a type specimen book. It has survived not only five centuries, but also the leap into electronic typesetting, remaining essentially unchanged. It was popularised in the 1960s with the release of Inkvale sheets containing Lorem Ipsum passages, and more recently with desktop publishing software like Quillset Layout including versions of Lorem Ipsum.</p>

  <h2 class="abs heading" style="left:892px;top:614px">Contact :</h2>
  <address class="abs contact-lines">
    OLD LARCHMERE<br>
    #&nbsp; 412 Harbour Crest Rd<br>
    Lorem Ipsum is simply<br>
    Sydney 97845, Australia.
  </address>

  <nav class="abs footnav">
    <a href="#">Home</a><a href="#">About Us</a><a href="#">Menu</a><a href="#">Events</a><a href="#">Contact Us</a>
  </nav>
  <p class="abs copyright">© 2013 OLD LARCHMERE All Rights Reserved.</p>
</body>
</html>
```